Redesign website for small print company

Vindabrot is a small printing company in Iceland mainly servicing Students, schools, etc. We are also doing all kind of other jobs, like business cards, book printing, brochure printing etc. We are also selling books online.
Our website is: www.vindabrot.is
What we are looking for is:
- Web Design (Uncoded - PSD layout only)
- Mobile friendly design, using our current color scheme: Red, green, yellow and light gray.
- Clean simple design
- Simple, light and easy to use.
- More menu Items/drop down
Industry/Entity Type
Digital Printing
Number of Pages Required
5+ page
Requirements
Must have
- Easy navigation
- Designed for mobile
- Current color scheme (see logo)
Nice to have
- Icon based products

```html
<!DOCTYPE html>
<html lang="is">
<head>
<meta charset="utf-8">
<title>Vindabrot – Prentþjónusta</title>
<link href="https://fonts.googleapis.com/css2?family=Montserrat:wght@400;500;600;700;800&display=swap" rel="stylesheet">
<style>
:root{
  --red:#e8202a;
  --red-dark:#c3161f;
  --green:#22a45d;
  --yellow:#f7c600;
  --grey-bg:#f3f3f3;
  --grey-mid:#6d6d6d;
  --ink:#1d1d1d;
  --text:#555;
  --line:#e2e2e2;
  --white:#fff;
}
*{box-sizing:border-box;margin:0;padding:0}
html,body{width:1200px;height:3358px;overflow:hidden}
body{position:relative;background:var(--white);font-family:'Montserrat',sans-serif;color:var(--ink)}
.abs{position:absolute}

/* header */
.site-header{position:absolute;left:0;top:0;width:1200px;height:56px;background:var(--white);z-index:5}
.logo-box{position:absolute;left:96px;top:0;width:234px;height:78px;background:var(--white);box-shadow:0 2px 8px rgba(0,0,0,.18);display:flex;align-items:center;justify-content:center;gap:10px;z-index:6}
.logo-mark{width:22px;height:22px;background:var(--red)}
.logo-name{font-weight:800;font-size:21px;color:var(--ink);letter-spacing:.5px}
.main-nav{position:absolute;left:560px;top:0;height:56px;display:flex;align-items:center;gap:46px}
.main-nav a{font-size:12px;font-weight:700;color:var(--ink);text-decoration:none;position:relative;height:56px;display:flex;align-items:center}
.main-nav a.active::before{content:"";position:absolute;top:0;left:0;right:0;height:4px;background:var(--green)}
.nav-icons{position:absolute;left:1016px;top:14px;display:flex;gap:12px}

/* hero */
.hero{position:absolute;left:0;top:56px;width:1200px;height:544px;background:linear-gradient(180deg,#f0312b 0%,#e8202a 60%,#d91a22 100%);overflow:hidden}
.hero-ghost{position:absolute;left:-20px;top:70px;font-size:170px;font-weight:800;color:rgba(0,0,0,.08);letter-spacing:6px}
.hero-ghost.right{left:820px;top:400px}
.hero-photo{position:absolute;left:448px;top:0;width:325px;height:544px;background:linear-gradient(180deg,#d9b48c 0%,#9a9a9a 45%,#5b6f8a 100%)}
.ribbon{position:absolute;background:var(--red-dark);color:var(--white);font-weight:800;font-size:30px;display:flex;align-items:center;box-shadow:0 3px 6px rgba(0,0,0,.25)}
.ribbon.left{left:132px;top:320px;width:300px;height:62px;padding-left:16px;transform:rotate(-2deg)}
.ribbon.right{left:740px;top:294px;width:316px;height:62px;padding-left:12px;transform:rotate(3deg)}
.hero-dots{position:absolute;left:568px;top:468px;display:flex;gap:6px}
.hero-dots span{width:9px;height:9px;border-radius:50%;background:rgba(255,255,255,.7)}
.hero-dots span.on{background:var(--white)}

/* products */
.section-title{position:absolute;left:0;width:1200px;text-align:center;font-weight:800;font-size:29px}
.section-title .accent{color:var(--green)}
.section-sub{position:absolute;left:0;width:1200px;text-align:center;font-size:15px;color:#9a9a9a;line-height:21px}
.product-card{position:absolute;width:302px;height:370px;background:var(--white);box-shadow:0 2px 8px rgba(0,0,0,.14);padding:12px}
.product-card .thumb{width:278px;height:190px}
.thumb.signs{background:linear-gradient(90deg,#2f8a3c 0%,#c94a2a 45%,#2f6db3 80%,#3a3a3a 100%)}
.thumb.books{background:linear-gradient(135deg,#2bb3b0 0%,#1e7e86 40%,#6b3b22 70%,#e9e4d6 100%)}
.thumb.cards{background:linear-gradient(135deg,#f2f2f2 0%,#d7d7d7 40%,#1f1f1f 60%,#7fbf2a 100%)}
.product-card h3{font-size:16px;font-weight:700;margin:26px 0 12px}
.product-card p{font-size:12px;line-height:19px;color:var(--text);width:240px}
.btn-outline{display:inline-block;margin-top:18px;padding:6px 18px;border:1px solid #bbb;font-size:10px;color:var(--ink)}
.btn-solid{display:inline-block;margin-top:18px;padding:7px 19px;background:var(--green);font-size:10px;font-weight:700;color:var(--white)}

/* welcome */
.welcome{position:absolute;left:0;top:1605px;width:1200px;height:640px;background:var(--grey-bg)}
.welcome-text{position:absolute;left:157px;top:76px;width:500px}
.welcome-text h2{font-size:30px;font-weight:700;margin-bottom:20px}
.welcome-text h2 span{color:var(--red)}
.welcome-text .lead{font-size:16px;font-weight:600;line-height:27px;margin-bottom:24px}
.welcome-text p{font-size:14px;line-height:27px;color:var(--text);margin-bottom:26px}
.photo-frame{position:absolute;background:var(--white);padding:8px;box-shadow:0 3px 10px rgba(0,0,0,.2)}
.photo-frame div{width:100%;height:100%}

/* features */
.feature{position:absolute;width:190px;text-align:center}
.feature .icon{height:56px;display:flex;justify-content:center;align-items:flex-end;margin-bottom:16px}
.feature h4{font-size:12px;font-weight:700;line-height:16px;margin-bottom:14px}
.feature p{font-size:11px;line-height:18px;color:var(--text);padding:0 22px}
.feature .tag{display:inline-block;margin-top:16px;padding:6px 14px;font-size:10px;font-weight:700;color:var(--white)}
.feature.boxed{background:var(--white);box-shadow:0 2px 12px rgba(0,0,0,.18);padding-top:22px;height:258px}

/* testimonials */
.testimonials{position:absolute;left:0;top:2635px;width:1200px;height:392px;background:var(--grey-bg)}
.quote-card{position:absolute;top:78px;width:300px;height:146px;background:var(--white);border-radius:6px;box-shadow:0 1px 5px rgba(0,0,0,.1);padding:28px 30px;text-align:center;font-size:11px;line-height:19px;color:var(--text)}
.quote-card::after{content:"";position:absolute;left:212px;bottom:-14px;border-left:14px solid transparent;border-right:0 solid transparent;border-top:14px solid var(--white)}
.quote-mark{display:inline-block;font-size:26px;font-weight:800;line-height:10px;vertical-align:-10px;margin-left:6px}
.author{position:absolute;top:272px;display:flex;align-items:center;gap:10px}
.author .who{text-align:right;font-size:11px;line-height:15px}
.author .who b{font-weight:700;color:var(--ink)}
.author .who span{color:var(--text)}
.avatar{width:52px;height:52px;border-radius:50%;background:linear-gradient(180deg,#b9b9b9,#6f6f6f);border:2px solid var(--white)}
.slider-dots{position:absolute;left:544px;top:346px;display:flex;gap:8px}
.slider-dots span{width:9px;height:9px;border-radius:50%;background:#cfcfcf}
.slider-dots span.on{background:var(--red)}

/* footer */
.newsletter-title{position:absolute;left:192px;top:3060px;font-size:16px;font-weight:700;line-height:22px}
.newsletter-title span{color:var(--red)}
.field{position:absolute;top:3073px;height:34px;border:1px solid var(--line);background:var(--white);font-size:11px;padding:10px 8px;color:#444}
.btn-subscribe{position:absolute;left:884px;top:3073px;width:114px;height:34px;background:var(--red);color:var(--white);font-size:11px;font-weight:700;display:flex;align-items:center;justify-content:center}
.footer-logo{position:absolute;left:190px;top:3166px;display:flex;align-items:center;gap:8px}
.footer-logo .logo-mark{width:20px;height:20px}
.footer-logo .logo-name{font-size:18px}
.contact{position:absolute;left:190px;top:3204px;font-size:11px;line-height:24px;color:var(--ink)}
.contact div{display:flex;align-items:center;gap:8px}
.footer-col{position:absolute;top:3152px;font-size:11px;line-height:21px;color:var(--ink)}
.footer-col h5{font-size:13px;font-weight:700;margin-bottom:4px}
.footer-rule{position:absolute;left:190px;top:3310px;width:820px;height:1px;background:var(--line)}
.copyright{position:absolute;left:190px;top:3322px;font-size:10px;color:var(--ink)}
.socials{position:absolute;left:950px;top:3318px;display:flex;gap:6px}
.socials span{width:15px;height:15px;border-radius:50%;border:1px solid #777}
</style>
</head>
<body>

<header class="site-header">
  <div class="logo-box"><span class="logo-mark"></span><span class="logo-name">VINDABROT</span></div>
  <nav class="main-nav">
    <a href="#">HEIM</a>
    <a href="#" class="active">ÞJÓNUSTA</a>
    <a href="#">SKIL Á VERKUM</a>
    <a href="#">UM OKKUR</a>
  </nav>
  <div class="nav-icons">
    <svg width="28" height="24" viewBox="0 0 28 24"><path d="M1 3h4l3 12h14l3-9H7" fill="none" stroke="#1d1d1d" stroke-width="2"/><circle cx="10" cy="20" r="2" fill="#1d1d1d"/><circle cx="20" cy="20" r="2" fill="#1d1d1d"/><circle cx="22" cy="5" r="5" fill="#e8202a"/></svg>
    <svg width="24" height="24" viewBox="0 0 24 24"><circle cx="10" cy="10" r="7" fill="none" stroke="#1d1d1d" stroke-width="2.4"/><path d="M15 15l7 7" stroke="#1d1d1d" stroke-width="2.6"/></svg>
  </div>
</header>

<section class="hero">
  <div class="hero-ghost">PRINT</div>
  <div class="hero-ghost right">DESIG</div>
  <div class="hero-photo" role="img" aria-label="Ljósmynd af ungri konu í gráum prentuðum stuttermabol með sólgleraugu"></div>
  <div class="ribbon left">READY TO PRINT</div>
  <div class="ribbon right">AMAZING WORK</div>
  <div class="hero-dots"><span></span><span class="on"></span><span></span><span></span><span></span></div>
</section>

<h2 class="section-title" style="top:648px">VÖRUFL<span class="accent">OKKAR</span></h2>
<p class="section-sub" style="top:690px">Only Professionals for Only High<br>Quality Product</p>

<article class="product-card" style="left:128px;top:761px">
  <div class="thumb signs" role="img" aria-label="Ljósmynd af litríkum veggspjöldum á sýningarvegg"></div>
  <h3>veggspjöld</h3>
  <p>Lorem ipsum dolor sit amet, consectetuer adipiscing elit. Aenean commodo ligula eget dolor.</p>
  <span class="btn-outline">Read More</span>
</article>
<article class="product-card" style="left:455px;top:761px">
  <div class="thumb books" role="img" aria-label="Ljósmynd af innbundnum bókum og penna"></div>
  <h3>Bokaprentum</h3>
  <p>Lorem ipsum dolor sit amet, consectetuer adipiscing elit. Aenean commodo ligula eget dolor.</p>
  <span class="btn-outline">Read More</span>
</article>
<article class="product-card" style="left:784px;top:761px">
  <div class="thumb cards" role="img" aria-label="Ljósmynd af prentuðum nafnspjöldum"></div>
  <h3>Nafnspjod</h3>
  <p>Lorem ipsum dolor sit amet, consectetuer adipiscing elit. Aenean commodo ligula eget dolor.</p>
  <span class="btn-solid">Read More</span>
</article>

<article class="product-card" style="left:128px;top:1157px">
  <div class="thumb signs" role="img" aria-label="Ljósmynd af skiltum og merkingum á vegg"></div>
  <h3>Signage Material</h3>
  <p>Lorem ipsum dolor sit amet, consectetuer adipiscing elit. Aenean commodo ligula eget dolor.</p>
  <span class="btn-outline">Read More</span>
</article>
<article class="product-card" style="left:455px;top:1157px">
  <div class="thumb books" role="img" aria-label="Ljósmynd af innbundnum bókum og penna"></div>
  <h3>Bokaprentum</h3>
  <p>Lorem ipsum dolor sit amet, consectetuer adipiscing elit. Aenean commodo ligula eget dolor.</p>
  <span class="btn-outline">Read More</span>
</article>
<article class="product-card" style="left:784px;top:1157px">
  <div class="thumb cards" role="img" aria-label="Ljósmynd af prentuðum nafnspjöldum"></div>
  <h3>Nafnspjod</h3>
  <p>Lorem ipsum dolor sit amet, consectetuer adipiscing elit. Aenean commodo ligula eget dolor.</p>
  <span class="btn-outline">Read More</span>
</article>

<section class="welcome">
  <div class="welcome-text">
    <h2>Velkomin í <span>Vindabrot</span></h2>
    <p class="lead">Vindabrot er fyrirtæki staðsett á háskólasvæðinu sem hefur sérhæft sig í að þjónusta skólafólk, ásamt því að sinna allri almennri prentun fyrir almenning.</p>
    <p>Vindabrot gefur út greinasöfn og frumsamdar kennslubækur fyrir námskeið, prentar lokaritgerðir fyrir nema, auk þess að vinna við ótalinn fjölda smærri verka fyrir nemendur, kennara og stofnanir. Má þar nefna bæklinga, skýrslur, spurningalista, nafnspjöld, bækur, OCR skönnun og fleira.</p>
    <p>Vindabrot er laufvottuð prentsmiðja, Laufmerkið er opinbert umhverfismerki Norðurlandanna, sem hefur skapað sér fótfestu hér á landi og er þekkt meðal neytenda.</p>
    <p>Vindabrot er staðsett á horninu á Hlíðargötu og Norðurgötu. (gengið inn Norðurgötumegin)</p>
  </div>
  <div class="photo-frame" style="left:750px;top:95px;width:280px;height:330px"><div role="img" aria-label="Ljósmynd af brosandi nemendum" style="background:linear-gradient(160deg,#c9d6e4 0%,#d97aa0 45%,#3b4f7a 100%)"></div></div>
  <div class="photo-frame" style="left:694px;top:305px;width:230px;height:232px"><div role="img" aria-label="Ljósmynd af litaprufuspjöldum" style="background:linear-gradient(135deg,#f4f4f4 0%,#d9327a 35%,#5a3fa0 60%,#f1a21b 85%)"></div></div>
</section>

<div class="feature" style="left:218px;top:2330px">
  <div class="icon"><svg width="58" height="44" viewBox="0 0 58 44"><rect x="2" y="6" width="34" height="26" fill="#e8202a"/><path d="M36 14h12l8 10v8H36z" fill="#c3161f"/><circle cx="14" cy="36" r="6" fill="#1d1d1d"/><circle cx="44" cy="36" r="6" fill="#1d1d1d"/></svg></div>
  <h4>Shipping<br>by Currier</h4>
  <p>Lorem ipsum dolor sit amet, consectetuer adipiscing elit. Aenean commodo ligula</p>
  <span class="tag" style="background:var(--red)">Read More</span>
</div>
<div class="feature" style="left:409px;top:2330px">
  <div class="icon"><svg width="50" height="50" viewBox="0 0 50 50"><path d="M25 3l21 10v24L25 47 4 37V13z" fill="#22a45d"/><path d="M4 13l21 10 21-10M25 23v24" fill="none" stroke="#1d1d1d" stroke-width="2.5"/></svg></div>
  <h4>Registered<br>Mail Delivery</h4>
  <p>Lorem ipsum dolor sit amet, consectetuer adipiscing elit. Aenean commodo ligula</p>
  <span class="tag" style="background:var(--green)">Read More</span>
</div>
<div class="feature boxed" style="left:612px;top:2317px">
  <div class="icon"><svg width="50" height="50" viewBox="0 0 50 50"><circle cx="25" cy="25" r="22" fill="none" stroke="#1d1d1d" stroke-width="3"/><circle cx="25" cy="14" r="3" fill="#1d1d1d"/><rect x="22" y="21" width="6" height="17" fill="#1d1d1d"/></svg></div>
  <h4>Perfect<br>Customer Service</h4>
  <p>Lorem ipsum dolor sit amet, consectetuer adipiscing elit. Aenean commodo ligula</p>
  <span class="tag" style="background:var(--grey-mid)">Read More</span>
</div>
<div class="feature" style="left:812px;top:2330px">
  <div class="icon"><svg width="54" height="52" viewBox="0 0 54 52"><path d="M2 42l14-8 12 8 12-8 12 8-12 8-12-8-14 8z" fill="none" stroke="#1d1d1d" stroke-width="2"/><path d="M27 2c-8 0-13 6-13 13 0 9 13 23 13 23s13-14 13-23c0-7-5-13-13-13z" fill="#f7c600"/><circle cx="27" cy="15" r="5" fill="#fff"/></svg></div>
  <h4>Check Areas<br>We Ship Outside City</h4>
  <p>Lorem ipsum dolor sit amet, consectetuer adipiscing elit. Aenean commodo ligula</p>
  <span class="tag" style="background:var(--yellow)">Read More</span>
</div>

<section class="testimonials">
  <svg class="abs" style="left:44px;top:188px" width="14" height="22" viewBox="0 0 14 22"><path d="M12 2L3 11l9 9" fill="none" stroke="#aaa" stroke-width="3"/></svg>
  <svg class="abs" style="left:1136px;top:188px" width="14" height="22" viewBox="0 0 14 22"><path d="M2 2l9 9-9 9" fill="none" stroke="#e8202a" stroke-width="3"/></svg>

  <div class="quote-card" style="left:105px">Lorem ipsum dolor sit amet, consectetuer adipiscing elit. Aenean commodo ligula eget dolor. Aenean massa. Cum sociis natoque penatibus et magnisso<span class="quote-mark" style="color:var(--red)">”</span></div>
  <div class="quote-card" style="left:437px">Lorem ipsum dolor sit amet, consectetuer adipiscing elit. Aenean commodo ligula eget dolor. Aenean massa. Cum sociis natoque penatibus et magnisso<span class="quote-mark" style="color:var(--green)">”</span></div>
  <div class="quote-card" style="left:768px">Lorem ipsum dolor sit amet, consectetuer adipiscing elit. Aenean commodo ligula eget dolor. Aenean massa. Cum sociis natoque penatibus et magnisso<span class="quote-mark" style="color:var(--yellow)">”</span></div>

  <div class="author" style="left:158px"><div class="who"><b>Ari Magnússon, CEO</b><br><span>Company Name</span></div><div class="avatar" role="img" aria-label="Portrettmynd af viðskiptavini"></div></div>
  <div class="author" style="left:490px"><div class="who"><b>Ari Magnússon, CEO</b><br><span>Company Name</span></div><div class="avatar" role="img" aria-label="Portrettmynd af viðskiptavini"></div></div>
  <div class="author" style="left:820px"><div class="who"><b>Ari Magnússon, CEO</b><br><span>Company Name</span></div><div class="avatar" role="img" aria-label="Portrettmynd af viðskiptavini"></div></div>

  <div class="slider-dots"><span></span><span></span><span class="on"></span><span></span><span></span></div>
</section>

<footer>
  <div class="newsletter-title">Subscribe<br><span>For Our Newsletter</span></div>
  <div class="field" style="left:459px;width:140px">Full Name.</div>
  <div class="field" style="left:611px;width:230px">Email Address.</div>
  <div class="btn-subscribe">Subscribe</div>

  <div class="footer-logo"><span class="logo-mark"></span><span class="logo-name">VINDABROT</span></div>
  <div class="contact">
    <div><svg width="12" height="12" viewBox="0 0 12 12"><path d="M2 1l2.5 0 1 3-1.5 1c.7 1.4 1.6 2.3 3 3l1-1.5 3 1V11C6 11 1 6 1 2z" fill="#e8202a"/></svg>+354 555 0142</div>
    <div><svg width="12" height="10" viewBox="0 0 12 10"><rect width="12" height="10" fill="#e8202a"/><path d="M0 0l6 5 6-5" fill="none" stroke="#fff" stroke-width="1.2"/></svg>info@vindabrot.is</div>
    <div style="padding-left:20px">Company Name</div>
  </div>

  <div class="footer-col" style="left:425px"><h5 style="color:var(--red)">About Vindabrot</h5>Newsletter<br>Our Memberships<br>Events<br>Investors<br>Suppliers Response</div>
  <div class="footer-col" style="left:660px"><h5 style="color:var(--green)">Account</h5>Manage Your ID<br>Vindabrot Store<br>Customer Reviews<br>Ask a Question<br>Why choose us?</div>
  <div class="footer-col" style="left:873px"><h5 style="color:var(--yellow)">Inclusion</h5>Inclusion and Diversity<br>Supplier Responsibility<br>Inclusion and Diversity<br>Shop for Business<br>Shop for Consumers</div>

  <div class="footer-rule"></div>
  <div class="copyright">Copyright 2018 Vindabrot | All rights reserved</div>
  <div class="socials"><span></span><span></span><span></span></div>
</footer>

</body>
</html>
```